Product Menu 8 x 11- Home Inspection Company Ancillary Services

Hello, on the front side of the flyer will be all about sewer camera inspections. These will include the images of the damages on the front and the information on the Sewer Scope Inspections: Safeguard Your Home from Hidden Plumbing Issues.
On the back will include indoor air quality. Solar Panel Inspections, Roof Certifications, and Expert Raised Foundation Review.
Please use logo and colors as a branding guide for the flyer.
$275- Sewer Camera Fee
$495 -Indoor Air Quality Inspection- Getting an indoor air quality (IAQ) inspection for mold when buying a home is crucial for health, safety, and financial protection. Mold can cause serious respiratory issues, especially for those with allergies or asthma, and toxic molds like black mold pose additional risks. It often grows in hidden areas, such as behind walls or in HVAC systems, often linked to water damage or structural issues. Early detection allows you to negotiate remediation costs, prevent mold from spreading, and avoid expensive repairs, ensuring a safe and sound investment.
$395 -Solar Panel Inspection- Getting a solar panel inspection when buying a home is essential to ensure efficiency, safety, and long-term savings. It verifies the system’s condition, identifying issues like damaged panels, faulty wiring, or inefficient inverters that could impact performance or pose safety risks. The inspection also evaluates the system’s energy output and compatibility with your energy needs, ensuring you’re benefiting from the investment. Additionally, understanding the age, warranty, and maintenance history of the system helps avoid unexpected repair costs and maximizes the value of this eco-friendly feature.
$399 Roof Certifications- Obtaining a roof certification when buying a home is vital for assessing the roof's condition, lifespan, and potential repair needs. This certification provides a professional evaluation, ensuring the roof is free from leaks, damage, or structural issues, which could lead to costly repairs. Many insurance companies require a roof certification before issuing or renewing a policy, particularly for older roofs, to confirm it meets safety standards. Having this certification not only provides peace of mind but also helps facilitate insurance coverage and protects your investment in the property.
$199- Advanced Foundation Review-An advanced foundation review by a licensed foundation contractor is essential when buying a home, as it provides a detailed assessment beyond what a general home inspector can offer. While home inspectors are trained generalists who identify visible issues, a foundation contractor is a specialist with the expertise to evaluate structural integrity, detect hidden problems, and determine the severity of any concerns. This specialized review can uncover issues like uneven settling, cracks, or drainage problems that may require repairs, ensuring you have a clear understanding of the foundation's condition before making a significant investment.
Real Estate Buyers and Real Estate Agents

```html
<!DOCTYPE html>
<html lang="en">
<head>
<meta charset="utf-8">
<title>Summit Crest Inspections – Ancillary Services Menu</title>
<link href="https://fonts.googleapis.com/css2?family=Oswald:wght@500;600&family=Source+Sans+3:wght@400;600;700&display=swap" rel="stylesheet">
<style>
:root{
  --blue:#0f62b5;
  --blue-dark:#0b4f95;
  --red:#dd3440;
  --ink:#1d1d1f;
  --white:#ffffff;
  --stage:#555a6b;
  --gold:#c9a437;
  --bronze:#8d8571;
}
*{margin:0;padding:0;box-sizing:border-box}
html,body{width:1200px;height:904px;overflow:hidden}
body{background:var(--stage);font-family:"Source Sans 3",Arial,sans-serif;color:var(--ink);position:relative}
.page{position:absolute;top:126px;width:505px;height:651px;background:var(--white);overflow:hidden}
.page--front{left:85px}
.page--back{left:616px}
.abs{position:absolute}

/* brand block */
.brand{display:flex;flex-direction:column;align-items:center;gap:5px}
.brand__mark{width:72px;height:72px;border-radius:50%;background:var(--red)}
.brand__name{font-family:"Oswald",sans-serif;font-weight:600;font-size:15px;letter-spacing:.5px;color:var(--blue);text-transform:uppercase;white-space:nowrap}
.brand--front{left:14px;top:14px;width:175px}
.brand--back{left:230px;top:572px;flex-direction:row;gap:8px}
.brand--back .brand__mark{width:40px;height:40px}
.brand--back .brand__name{font-size:16px}

/* hero */
.hero{left:0;top:0;width:505px;height:224px}
.hero__title{left:29px;top:137px;width:210px;font-family:"Oswald",sans-serif;font-weight:500;font-size:17.5px;line-height:20px;color:var(--white)}
.badge{width:62px;height:62px;border-radius:50%;top:178px;border:3px solid var(--white);box-shadow:0 1px 3px rgba(0,0,0,.35)}
.badge--red{left:275px;background:var(--red)}
.badge--gold{left:344px;background:var(--gold)}
.badge--bronze{left:413px;background:var(--bronze)}

/* front copy */
.h2{font-weight:700;font-size:15px;color:var(--blue);line-height:18px}
.lead{font-size:9.6px;line-height:12px}
.h2--what{left:29px;top:234px}
.lead--what{left:29px;top:252px;width:446px}
.h2--why{left:29px;top:303px}
.gallery{left:29px;top:326px;width:193px;display:grid;grid-template-columns:92px 92px;grid-auto-rows:91px;gap:6px 8px}
.gallery__shot{border-radius:3px;border:1px solid #cfcfcf}
.reasons{left:237px;top:324px;width:238px}
.reason{margin-bottom:5px}
.reason__title{font-weight:600;font-size:11.5px;line-height:13px;color:var(--red)}
.reason__text{font-size:8.1px;line-height:10.4px;text-align:justify}

/* footer */
.footer{left:0;bottom:0;width:505px;height:32px;display:flex;font-size:9.5px;color:var(--white)}
.footer__cell{display:flex;align-items:center;gap:5px;padding-left:29px}
.footer__cell:nth-child(1){width:160px;background:var(--red)}
.footer__cell:nth-child(2){width:184px;background:var(--blue);padding-left:9px}
.footer__cell:nth-child(3){width:161px;background:var(--red);padding-left:7px}
.footer__icon{width:12px;height:12px;flex:none}

/* back */
.topband{left:0;top:0;width:505px;height:7px;display:flex}
.topband span:nth-child(1){width:160px;background:var(--red)}
.topband span:nth-child(2){width:184px;background:var(--blue)}
.topband span:nth-child(3){width:161px;background:var(--red)}
.service__photo{left:28px;width:121px;border-radius:3px;border:1px solid #cfcfcf}
.service__body{left:168px;width:309px;font-size:7.7px;line-height:9.9px;text-align:justify}
.price{float:left;width:48px;height:48px;margin:0 7px 2px 0;border-radius:50%;background:var(--blue);shape-outside:circle(50%);color:var(--white);font-family:"Oswald",sans-serif;font-weight:500;font-size:17px;display:flex;align-items:center;justify-content:center;letter-spacing:-.3px}
.service__title{font-weight:600;font-size:11.5px;line-height:13px;color:var(--red);text-align:left}
</style>
</head>
<body>

<!-- FRONT -->
<section class="page page--front">
  <svg class="abs hero" viewBox="0 0 505 224" aria-hidden="false">
    <defs>
      <radialGradient id="pipe" cx="0.55" cy="0.3" r="0.75">
        <stop offset="0" stop-color="#3b2f22"/>
        <stop offset="0.35" stop-color="#7a6250"/>
        <stop offset="0.75" stop-color="#b3a28a"/>
        <stop offset="1" stop-color="#8f8270"/>
      </radialGradient>
    </defs>
    <polygon points="193,0 505,0 505,206 245,206" fill="url(#pipe)" role="img" aria-label="Camera view inside a sewer pipe with tree root intrusion"/>
    <polygon points="186,0 193,0 248,206 240,206" fill="#0f62b5"/>
    <polygon points="0,128 224,128 246,206 0,206" fill="#0f62b5"/>
    <rect x="0" y="206" width="505" height="3" fill="#ffffff"/>
    <rect x="0" y="209" width="505" height="13" fill="#dd3440"/>
  </svg>

  <div class="abs brand brand--front">
    <span class="brand__mark"></span>
    <span class="brand__name">Summit Crest Inspections</span>
  </div>

  <h1 class="abs hero__title">Sewer Camera Inspection: Safeguard Your Home from Hidden Plumbing Issues</h1>

  <span class="abs badge badge--red"></span>
  <span class="abs badge badge--gold"></span>
  <span class="abs badge badge--bronze"></span>

  <h2 class="abs h2 h2--what">What is a Sewer Camera Inspection?</h2>
  <p class="abs lead lead--what">A sewer camera inspection uses a camera to inspect your home's sewer lines. The camera is inserted into the sewer pipe, allowing an inspector to detect blockages, cracks, tree root intrusions, and other issues that can cause significant damage if left unaddressed.</p>

  <h2 class="abs h2 h2--why">Why You Should Get a Sewer Camera Inspection:</h2>

  <div class="abs gallery">
    <div class="gallery__shot" role="img" aria-label="Dark pipe interior with joint" style="background:radial-gradient(circle at 55% 50%,#1a1a1a,#4d4d4d 45%,#8a8a8a)"></div>
    <div class="gallery__shot" role="img" aria-label="Scaled pipe interior" style="background:radial-gradient(circle at 65% 45%,#2a2a26,#8c8a7a 45%,#c9c6b6)"></div>
    <div class="gallery__shot" role="img" aria-label="Rusted pipe opening" style="background:radial-gradient(circle at 50% 40%,#1b0d06,#7a3410 40%,#c48a6a 60%,#5d6d6a)"></div>
    <div class="gallery__shot" role="img" aria-label="Debris filled sewer tunnel" style="background:radial-gradient(circle at 50% 30%,#1e1e1e,#4a4a3e 45%,#6f6c55)"></div>
    <div class="gallery__shot" role="img" aria-label="Corroded pipe with buildup" style="background:radial-gradient(circle at 50% 50%,#1b140c,#6b4f2a 45%,#b8915a)"></div>
    <div class="gallery__shot" role="img" aria-label="Pipe with blue tinted deposits" style="background:radial-gradient(circle at 45% 55%,#120f14,#3b3a4a 40%,#5a7d8a 70%,#8a6a4a)"></div>
  </div>

  <div class="abs reasons">
    <div class="reason"><h3 class="reason__title">Prevent Costly Repairs,</h3><p class="reason__text">Sewer line issues can be extremely expensive to fix, with some repairs costing thousands of dollars. A sewer camera inspection can identify problems early, potentially saving you from dealing with costly repairs down the road.</p></div>
    <div class="reason"><h3 class="reason__title">Protect Your Investment</h3><p class="reason__text">Whether you're buying or selling a home, understanding the condition of the sewer system can impact your decision. For buyers, it helps avoid unexpected expenses. For sellers, it can provide peace of mind and ensure the sale goes smoothly.</p></div>
    <div class="reason"><h3 class="reason__title">Catch Hidden Problems</h3><p class="reason__text">Sewer line issues often remain hidden until it's too late. Without a sewer scope inspection, it's nearly impossible to identify problems that could lead to sewage backups, unpleasant odors, and costly damages.</p></div>
    <div class="reason"><h3 class="reason__title">Avoid Health Hazards</h3><p class="reason__text">Faulty sewer systems can lead to sewage backups, which are not only unpleasant but also pose serious health risks. Inspections help ensure your home's plumbing is functioning safely.</p></div>
    <div class="reason"><h3 class="reason__title">Ensure Proper Functioning</h3><p class="reason__text">A sewer scope inspection gives you a better understanding of how well your sewer system is functioning. It helps detect potential issues like blockages from tree roots, misaligned pipes, or wear and tear that may cause drainage problems.</p></div>
  </div>

  <footer class="abs footer">
    <div class="footer__cell"><svg class="footer__icon" viewBox="0 0 12 12"><circle cx="6" cy="6" r="5.5" fill="none" stroke="#fff"/><path d="M4 3.2l1 1.4-.6.6c.4.9 1 1.5 1.9 1.9l.6-.6 1.4 1-.6.9c-2 0-4.4-2.4-4.4-4.4z" fill="#fff"/></svg>800-555-0142</div>
    <div class="footer__cell"><svg class="footer__icon" viewBox="0 0 12 12"><circle cx="6" cy="6" r="5.5" fill="none" stroke="#fff"/><rect x="3" y="4" width="6" height="4.2" fill="none" stroke="#fff" stroke-width=".8"/><path d="M3 4l3 2.3L9 4" fill="none" stroke="#fff" stroke-width=".8"/></svg>hello@summitcrestinspect.com</div>
    <div class="footer__cell"><svg class="footer__icon" viewBox="0 0 12 12"><circle cx="6" cy="6" r="5.5" fill="none" stroke="#fff"/><ellipse cx="6" cy="6" rx="2.2" ry="5" fill="none" stroke="#fff" stroke-width=".7"/><path d="M1 6h10M1.8 3.5h8.4M1.8 8.5h8.4" stroke="#fff" stroke-width=".7"/></svg>www.summitcrestinspect.com</div>
  </footer>
</section>

<!-- BACK -->
<section class="page page--back">
  <div class="abs topband"><span></span><span></span><span></span></div>

  <div class="abs service__photo" style="top:25px;height:77px;background:linear-gradient(135deg,#c9ccc9,#8d9290 55%,#3b3f44)" role="img" aria-label="Inspector testing indoor air with a monitor"></div>
  <div class="abs service__body" style="top:24px">
    <span class="price">$495</span>
    <h3 class="service__title">Indoor Air Quality Inspection</h3>
    Getting an indoor air quality (IAQ) inspection for mold when buying a home is crucial for health, safety, &amp; financial protection. Mold can cause serious respiratory issues, especially for those with allergies or asthma, and toxic molds like black mold pose additional risks. It often grows in hidden areas, such as behind walls or in HVAC systems, often linked to water damage or structural issues. Early detection allows you to negotiate remediation costs, prevent mold from spreading, &amp; avoid expensive repairs, ensuring a safe &amp; sound investment.
  </div>

  <div class="abs service__photo" style="top:118px;height:77px;background:linear-gradient(135deg,#d8d8da,#a9a7a6 60%,#7b8fb5)" role="img" aria-label="Gloved hands swabbing a moldy wall"></div>
  <div class="abs service__body" style="top:134px">
    <span class="price">$100</span>
    <h3 class="service__title">Mold Swabs</h3>
    We use this test to swab stains and send to a labratory to determine if there is surface mold and identify what type it is.
  </div>

  <div class="abs service__photo" style="top:211px;height:85px;background:linear-gradient(180deg,#5b6b84,#c7b9a2 55%,#6f8a9a)" role="img" aria-label="House roof with solar panels and pool"></div>
  <div class="abs service__body" style="top:208px">
    <span class="price">$395</span>
    <h3 class="service__title">Solar Panel Inspection</h3>
    Getting a solar panel inspection when buying a home is essential to ensure efficiency, safety, and long-term savings. It verifies the system's condition, identifying issues like damaged panels, faulty wiring, or inefficient inverters that could impact performance or pose safety risks. The inspection also evaluates the system's energy output and compatibility with your energy needs, ensuring you're benefiting from the investment. Additionally, understanding the age, warranty, and maintenance history of the system helps avoid unexpected repair costs &amp; maximizes the value of this eco-friendly feature.
  </div>

  <div class="abs service__photo" style="top:312px;height:89px;background:linear-gradient(160deg,#6d8a5a,#a6a49a 50%,#5a5e66)" role="img" aria-label="Inspector with a ladder on a shingle roof"></div>
  <div class="abs service__body" style="top:312px">
    <span class="price">$399</span>
    <h3 class="service__title">Roof Certifications</h3>
    A roof certification serves as a guarantee from the roofer that any leaks occurring within two years will be repaired at no cost in the affected area. Homeowners also have the option to extend this coverage for up to five years. During the certification inspection, if defects are identified that render the roof ineligible, a detailed report will outline the necessary repairs required to meet certification standards, ensuring the roof is structurally sound and compliant.
  </div>

  <div class="abs service__photo" style="top:415px;height:90px;background:linear-gradient(180deg,#3c3a38,#8a8680 55%,#5f5a55)" role="img" aria-label="Raised foundation crawlspace with marked cracks"></div>
  <div class="abs service__body" style="top:428px">
    <span class="price">$199</span>
    <h3 class="service__title">Advanced Foundation Review</h3>
    This review is a digital review on raised foundations only. A licensed foundation contractor will review the images in our report and provide further evaluation as to any additional defects noted and the remedies to bring these to compliance.
  </div>

  <div class="abs service__photo" style="top:519px;height:87px;background:linear-gradient(135deg,#f2f2f2,#cfd3da 50%,#2f3f8a)" role="img" aria-label="Sewer camera reel and monitor case"></div>
  <div class="abs service__body" style="top:518px">
    <span class="price">$275</span>
    <h3 class="service__title">Sewer Camera Fee</h3>
    With the help of an advanced plumbing camera, this inspection gives us a full picture of your sewer lines and rule out any invasive tree roots, damage, breaks, and blockages.
  </div>

  <div class="abs brand brand--back">
    <span class="brand__mark"></span>
    <span class="brand__name">Summit Crest Inspections</span>
  </div>

  <footer class="abs footer">
    <div class="footer__cell"><svg class="footer__icon" viewBox="0 0 12 12"><circle cx="6" cy="6" r="5.5" fill="none" stroke="#fff"/><path d="M4 3.2l1 1.4-.6.6c.4.9 1 1.5 1.9 1.9l.6-.6 1.4 1-.6.9c-2 0-4.4-2.4-4.4-4.4z" fill="#fff"/></svg>800-555-0142</div>
    <div class="footer__cell"><svg class="footer__icon" viewBox="0 0 12 12"><circle cx="6" cy="6" r="5.5" fill="none" stroke="#fff"/><rect x="3" y="4" width="6" height="4.2" fill="none" stroke="#fff" stroke-width=".8"/><path d="M3 4l3 2.3L9 4" fill="none" stroke="#fff" stroke-width=".8"/></svg>hello@summitcrestinspect.com</div>
    <div class="footer__cell"><svg class="footer__icon" viewBox="0 0 12 12"><circle cx="6" cy="6" r="5.5" fill="none" stroke="#fff"/><ellipse cx="6" cy="6" rx="2.2" ry="5" fill="none" stroke="#fff" stroke-width=".7"/><path d="M1 6h10M1.8 3.5h8.4M1.8 8.5h8.4" stroke="#fff" stroke-width=".7"/></svg>www.summitcrestinspect.com</div>
  </footer>
</section>

</body>
</html>
```